PLAV Brochure Design Project

I need a brochure for my new project management company.
the scope covers all engineering aspects of developments.
Green design is also included. so, I would like to see colours representing the industry and sustainability. soft colours really.
Hello, I'm attaching herewith the text, images, and the logo that i want to appear on the brochure
Target Market(s)
developers, investors, governments
Industry/Entity Type
Industry
Look and feel

```html
<!DOCTYPE html>
<html lang="en">
<head>
<meta charset="utf-8">
<title>PLAV Project Management Brochure</title>
<link href="https://fonts.googleapis.com/css2?family=Questrial&display=swap" rel="stylesheet">
<style>
:root{
  --stage:#e4e2de;
  --navy-deep:#13205a;
  --navy:#1d2f78;
  --navy-mid:#274295;
  --sky:#5e92d8;
  --sky-light:#86b3ea;
  --sky-pale:#b8d6f6;
  --ink-light:#eaf2ff;
  --accent:#9fe0a8;
  --cyan:#8fcaff;
}
*{margin:0;padding:0;box-sizing:border-box}
html,body{width:1200px;height:442px;overflow:hidden;background:var(--stage)}
body{position:relative;font-family:"Questrial",sans-serif;color:var(--ink-light)}
.spread{position:absolute;top:21px;width:580px;height:400px;overflow:hidden;
  background:linear-gradient(180deg,var(--navy-deep) 0%,var(--navy) 55%,var(--navy-mid) 100%);
  box-shadow:0 3px 10px rgba(0,0,0,.25)}
.spread--cover{left:14px}
.spread--inside{left:606px}
.page{position:absolute;top:0;width:290px;height:400px}
.page--left{left:0}
.page--right{left:290px;border-left:1px solid rgba(255,255,255,.12)}
.photo{position:absolute}
.band{position:absolute;left:0;top:0}

/* cover back page */
.thumb{position:absolute;top:24px;height:50px;width:90px;clip-path:polygon(12% 0,100% 0,88% 100%,0 100%)}
.thumb--a{left:15px;background:linear-gradient(135deg,#2b2f3a,#8d919c 60%,#3b3f4a)}
.thumb--b{left:104px;background:linear-gradient(135deg,#cfd6c8,#6f9b6a 50%,#e8ece4)}
.thumb--c{left:193px;background:linear-gradient(135deg,#b9a786,#7f9a62 55%,#d7c8a8)}
.green-services{position:absolute;left:56px;top:124px}
.green-services h2{font-size:14px;font-weight:400;color:#fff;margin-bottom:9px}
.green-services li{list-style:none;font-size:7.6px;line-height:14.2px;color:#fff}
.green-services li::before{content:"";display:inline-block;width:3px;height:3px;background:var(--accent);margin-right:5px;vertical-align:middle}
.contact{position:absolute;left:18px;top:344px;display:flex;gap:8px}
.brand-mini{width:28px;text-align:center}
.brand-mini .square{display:block;width:22px;height:22px;background:var(--sky);margin:0 auto 2px}
.brand-mini b{font-size:7px;font-weight:400;color:#fff}
.contact ul{list-style:none;font-size:5.2px;line-height:8.3px;color:#cfe0ff}
.contact li::before{content:"";display:inline-block;width:3px;height:3px;border-radius:50%;background:var(--cyan);margin-right:3px;vertical-align:middle}

/* cover front page */
.brand{position:absolute;left:45px;top:14px;width:80px;text-align:center}
.brand .square{display:block;width:44px;height:44px;margin:0 auto 3px;background:var(--sky-light)}
.brand .name{font-size:13px;color:#fff;line-height:13px;letter-spacing:1px}
.brand .sub{font-size:5px;color:#cfe0ff;letter-spacing:.5px}
.city{left:1px;top:81px;width:289px;height:219px;background:linear-gradient(180deg,#c7c9c4 0%,#8d9398 40%,#6f8a5a 80%,#4f6c3d 100%)}
.tagline{position:absolute;left:0;width:290px;top:297px;text-align:center;font-size:14.5px;letter-spacing:.4px;color:#fff}
.url-tab{position:absolute;right:0;bottom:32px;width:135px;height:16px;background:var(--sky-light);clip-path:polygon(8% 0,100% 0,100% 100%,0 100%);font-size:6.5px;color:#fff;display:flex;align-items:center;padding-left:26px}
.url-tab::before,.bar-url::before{content:"";width:4px;height:4px;border-radius:50%;background:#2c56b0;margin-right:4px}

/* inside spread */
.section-title{font-size:13px;font-weight:400;color:#fff;position:absolute}
.body-copy{position:absolute;font-size:4.6px;line-height:5.9px;color:#e0ebff}
.body-copy p{margin-bottom:4px}
.about-title{left:22px;top:16px}
.about-copy{left:22px;top:34px;width:256px}
.map{top:139px;height:62px;background:linear-gradient(135deg,#3f5b3f,#7a9470 45%,#2f4a56 100%)}
.map--a{left:16px;width:118px}
.map--b{left:146px;width:134px}
.pm-title{left:22px;top:217px}
.pm-copy{left:22px;top:236px;width:256px;color:#fff}
.bar-url{position:absolute;left:0;bottom:6px;width:120px;height:14px;background:var(--sky-light);font-size:6.5px;color:#fff;display:flex;align-items:center;padding-left:12px}
.bar-phone{position:absolute;right:18px;bottom:9px;font-size:6.5px;color:#fff;display:flex;align-items:center;gap:3px}

.scope-title{left:11px;top:16px}
.scope-col{position:absolute;top:37px;width:95px}
.scope-col h4{font-size:4.9px;color:#fff;margin-bottom:1px}
.scope-col ul{list-style:none;margin-bottom:6px}
.scope-col li{font-size:4.5px;line-height:5.6px;color:#e0ebff;white-space:nowrap}
.scope-col li::before{content:"• ";color:var(--cyan)}
.col-1{left:11px}.col-2{left:99px}.col-3{left:190px}
.tower{left:11px;top:166px;width:71px;height:68px;background:linear-gradient(180deg,#dfe7f2,#8fa6c4 55%,#c9d6e6)}
.finance-title{left:120px;top:182px;font-size:11px}
.finance-list{position:absolute;left:128px;top:200px;list-style:none}
.finance-list li{font-size:4.6px;line-height:5.6px;color:#e0ebff}
.finance-list li::before{content:"• ";color:var(--cyan)}
.brand-corner{position:absolute;left:234px;top:189px;width:36px;text-align:center}
.brand-corner .square{display:block;width:26px;height:26px;background:var(--sky-light);margin:0 auto 2px}
.brand-corner b{font-size:7px;font-weight:400;color:#fff}
.render{top:250px;height:142px}
.render--a{left:11px;width:87px;background:linear-gradient(180deg,#d9dde2,#b7bcc4 60%,#9aa2ac)}
.render--b{left:102px;width:88px;background:linear-gradient(180deg,#11183a,#4a5f8a 55%,#2a2f3f)}
.render--c{left:195px;width:89px;background:linear-gradient(180deg,#d4dbe6,#b3c0d4 60%,#9aa6b8)}
</style>
</head>
<body>

<section class="spread spread--cover">
  <div class="page page--left">
    <svg class="band" width="290" height="400" viewBox="0 0 290 400" aria-hidden="true">
      <defs>
        <linearGradient id="bandFill" x1="0" y1="0" x2="1" y2="0">
          <stop offset="0" stop-color="#5e92d8"/>
          <stop offset="1" stop-color="#3d67bd"/>
        </linearGradient>
      </defs>
      <polygon points="0,100 120,100 105,114 290,114 290,297 0,297" fill="url(#bandFill)"/>
      <polygon points="0,100 120,100 105,114 0,114" fill="#86b3ea"/>
    </svg>
    <div class="photo thumb thumb--a" role="img" aria-label="Night render of a modern building"></div>
    <div class="photo thumb thumb--b" role="img" aria-label="Aerial render of a landscaped resort island"></div>
    <div class="photo thumb thumb--c" role="img" aria-label="Render of a mosque and surrounding development"></div>
    <div class="green-services">
      <h2>Our green services</h2>
      <ul>
        <li>Verdant Strategy, Certification &amp; Management</li>
        <li>Terralis Strategy, Certification &amp; Management</li>
        <li>Renewable Energy Feasibility</li>
        <li>Water Conservation Strategies</li>
        <li>Building Performance Assessments</li>
        <li>Sustainable Materials Cost Analysis</li>
        <li>Energy Modeling</li>
        <li>Mechanical System Options</li>
        <li>Carbon Advisory</li>
      </ul>
    </div>
    <div class="contact">
      <div class="brand-mini"><span class="square"></span><b>PLAV</b></div>
      <ul>
        <li>P.O. Box 1024, Harbor City</li>
        <li>+000 4 5550181</li>
        <li>+000 4 5550182</li>
        <li>www.plav-pm.net</li>
      </ul>
    </div>
  </div>
  <div class="page page--right">
    <div class="brand"><span class="square"></span><div class="name">PLAV</div><div class="sub">PROJECT MANAGEMENT</div></div>
    <div class="photo city" role="img" aria-label="Aerial 3D render of a high-rise city district with parks"></div>
    <div class="tagline">YOUR VISION OUR EXPERTISE</div>
    <div class="url-tab">www.plav-pm.net</div>
  </div>
</section>

<section class="spread spread--inside">
  <div class="page page--left">
    <svg class="band" width="290" height="400" viewBox="0 0 290 400" aria-hidden="true">
      <polygon points="0,210 262,210 290,238 290,400 0,400" fill="#5e92d8"/>
      <polygon points="0,210 262,210 276,224 0,224" fill="#7aa9e6"/>
    </svg>
    <h2 class="section-title about-title">About Us</h2>
    <div class="body-copy about-copy">
      <p>Since its establishment in 2005, PLAV has offered the highest quality services to leading enterprises belonging to several different industrial sectors. Aimed at achieving excellence and exposing innovation in all of our services, we have built a profile that is filled with project completion accomplishments marked by the highest quality, and all these have been done within the allotted budgets and exactly as scheduled.</p>
      <p>We provide Working Agreements and Alliance services and have developed considerable experience, which has helped us in gaining proficiency and quality in all our work. Many different organizations including both consultants and contractors, with roots spread throughout the country and across borders as well, have availed our services and built lasting business relationships with us.</p>
      <p>Our skill sets comprise of both technical and project management abilities which we use for providing assistance to our clients. We help them in several different projects that range from developing completely new models, processes or methodologies to applying current technologies for up-gradation of existing facilities.</p>
    </div>
    <div class="photo map map--a" role="img" aria-label="Satellite view of a coastal master plan site"></div>
    <div class="photo map map--b" role="img" aria-label="Satellite view of an offshore island development"></div>
    <h2 class="section-title pm-title">Our Project Management Services</h2>
    <div class="body-copy pm-copy">
      <p>We exhibit professionalism and have expertise in project management. We know exactly what it takes to help a team move forward and execute the projects successfully through all stages no matter what obstacles sprout up in the way.</p>
      <p>In the initial phases, we develop a complete understanding of our clients' goals. Based on this, we draft out a plan, finalize the sites and determine a suitable budget for the project. In the design development phase, we manage the strategies, build an executable model and help our clients balance the objectives, project constraints and associated risks. We analyze all possible procurement options, integrate the designs with the outcomes while ensuring that they lie in the budget, and translate all that is involved into a complete execution plan. In the control and delivery phase, we make sure the plan will fulfil the business needs and that we have taken all measures to minimize risks.</p>
      <p>We are an independent advisor and can give you suggestions and recommendations in a timely manner, such that the required design, planning and commercial inputs make it possible to achieve the required outcomes. We can provide advice in any aspect, be it market analysis, development strategies, layout mix and specification, marketing and implementation.</p>
      <p>The way in which we organize our projects helps us to maintain a sharper focus, increase efficiency and deliver outcomes in an effective manner. We have relationships with global enterprises, public sector companies and commercial occupiers.</p>
    </div>
    <div class="bar-url">www.plav-pm.net</div>
    <div class="bar-phone">
      <svg width="7" height="7" viewBox="0 0 10 10" aria-hidden="true"><path d="M2 1h2l1 2-1.2 1a6 6 0 0 0 2.2 2.2L7 5l2 1v2c0 .6-.4 1-1 1A8 8 0 0 1 1 2c0-.6.4-1 1-1z" fill="#fff"/></svg>
      +000 4 5550181
    </div>
  </div>
  <div class="page page--right">
    <svg class="band" width="290" height="400" viewBox="0 0 290 400" aria-hidden="true">
      <rect x="0" y="243" width="290" height="157" fill="#5e92d8"/>
    </svg>
    <h2 class="section-title scope-title">General Scope of Services</h2>
    <div class="scope-col col-1">
      <h4>Project analyses:</h4>
      <ul><li>Aerial Location &amp; Adjacent activities</li><li>Affection plan, area &amp; Accessibility</li><li>Photographic survey</li><li>Land profile &amp; special features</li><li>Site orientation</li><li>Advantages &amp; Disadvantages</li><li>Planning &amp; Building regulations</li><li>Climatic conditions</li><li>Segmental analyses</li><li>Site area analyses</li><li>Proposed planning model</li></ul>
      <h4>Contractual engagement:</h4>
      <ul><li>Scope of work</li><li>Draft agreement</li><li>Final agreement</li><li>Starting date</li></ul>
    </div>
    <div class="scope-col col-2">
      <h4>Project's baseline plan:</h4>
      <ul><li>Commercial brief</li><li>Estimated cost analyses</li><li>Estimated revenue analyses</li><li>Cash flow forecast</li><li>Investment model</li><li>Economical analyses</li><li>Progress program of work</li><li>Design &amp; construction logistics</li></ul>
      <h4>Formation of consortium:</h4>
      <ul><li>Invitation &amp; consolidation of interest</li><li>RFP &amp; Submission of offers</li><li>Tender analyses &amp; Awarding</li><li>Appointment of consultants</li></ul>
      <h4>Design development:</h4>
      <ul><li>Initial design study report</li><li>Single diagrammatic layout &amp; NOC's</li><li>Initial concept design</li><li>Third party review &amp; approvals</li><li>Update to baseline plan</li><li>Final design &amp; Tender documents</li></ul>
    </div>
    <div class="scope-col col-3">
      <h4>Tender &amp; Award:</h4>
      <ul><li>Pre-qualification &amp; short listing</li><li>Invitation &amp; confirmation on contribution</li><li>Tendering</li><li>Tender analyses &amp; Recommendation</li><li>Up date to baseline plan</li><li>Client's approval</li><li>Awarding</li></ul>
      <h4>Contractor's mobilization:</h4>
      <ul><li>Progress program</li><li>Method statements</li><li>Procurement plans</li><li>Tracking system</li><li>Client reports</li></ul>
      <h4>Construction works:</h4>
      <ul><li>Program management</li><li>Progress management</li><li>Cost management</li><li>Risk management</li></ul>
    </div>
    <div class="photo tower" role="img" aria-label="Render of twin glass towers joined by a sky bridge"></div>
    <h2 class="section-title finance-title">Financial Advisory</h2>
    <ul class="finance-list">
      <li>Financing plan</li><li>Financing structuring</li><li>Risk management</li><li>Banks liaison and interaction</li><li>Cash flow management</li><li>Project portfolio management</li>
    </ul>
    <div class="brand-corner"><span class="square"></span><b>PLAV</b></div>
    <div class="photo render render--a" role="img" aria-label="Site plan diagram with highlighted zones"></div>
    <div class="photo render render--b" role="img" aria-label="Night render of twin towers"></div>
    <div class="photo render render--c" role="img" aria-label="Daylight render of twin towers"></div>
  </div>
</section>

</body>
</html>
```